Business Card Design - Corporate

Create a sleek elegant business card layout while suggesting a color scheme. Convey cutting edge technology while maintaining a corporate feel that is easily readable.

Company designs and manufactures consumer electronic products for mass retail that are mainly app driven.

(vector logo and die-line provided)

Target Market(s)

Corporate level, tech industry.

Industry/Entity Type

Business

Contact Information for Business Card

Generic Info:

Name
Title
email
address
phone 1
phone 2
website (quillbarn.com) on back

Font styles to use
Sans Serif

Requirements
Must have
• At least 2 colors + white on one side.
Nice to have
• Solid suggestion on color for logo and overall design. Color flood on back of card.
Should not have
• background texture like... marble, stone, patterns or circuit boards

```html
<!DOCTYPE html>
<html lang="en">
<head>
<meta charset="utf-8">
<title>Quillbarn Business Card</title>
<link href="https://fonts.googleapis.com/css2?family=Open+Sans:wght@400;600;700&display=swap" rel="stylesheet">
<style>
  :root {
    --backdrop: #a0a0a0;
    --card-dark: #545454;
    --card-light: #d6d6d6;
    --pattern-tone: #cfcfcf;
    --ink-light: #ffffff;
    --ink-soft: #e6e6e6;
    --ink-dark: #4a4a4a;
    --rule: #f2f2f2;
  }
  * { margin: 0; padding: 0; box-sizing: border-box; }
  html, body {
    width: 1200px; height: 900px; overflow: hidden;
    background: var(--backdrop);
    font-family: "Open Sans", Arial, sans-serif;
  }
  .canvas { position: relative; width: 1200px; height: 900px; }

  .card {
    position: absolute; top: 275px; width: 477px; height: 294px; overflow: hidden;
  }
  .card--front {
    left: 116px; background: var(--card-dark);
    border-radius: 0 62px 0 62px;
    color: var(--ink-light);
  }
  .card--back {
    left: 622px; background: var(--card-light);
    border-radius: 62px 0 62px 0;
  }

  .wordmark {
    position: absolute; font-weight: 400; letter-spacing: 4px; line-height: 1;
    white-space: nowrap;
  }
  .card--front .wordmark {
    right: 26px; top: 64px; font-size: 36px; color: var(--ink-light);
  }
  .card--back .wordmark {
    left: 0; right: 0; text-align: center; top: 126px; font-size: 46px;
    color: var(--ink-dark); letter-spacing: 5px;
  }

  .person { position: absolute; left: 21px; top: 125px; }
  .person__name { font-size: 16px; font-weight: 600; letter-spacing: 0.3px; line-height: 20px; }
  .person__title { font-size: 13px; color: var(--ink-soft); line-height: 18px; }

  .divider {
    position: absolute; left: 0; right: 0; top: 181px; height: 2px; background: var(--rule);
  }

  .address {
    position: absolute; left: 25px; top: 220px;
    font-size: 13px; line-height: 18px; color: var(--ink-soft); font-style: normal;
  }

  .contacts {
    position: absolute; right: 25px; top: 212px; list-style: none;
    font-size: 13px; line-height: 17.5px; color: var(--ink-soft); text-align: right;
  }
  .contacts li { display: flex; align-items: center; justify-content: flex-end; gap: 7px; }
  .contacts svg { width: 9px; height: 9px; fill: var(--ink-soft); }

  .pattern-field {
    position: absolute; inset: 0; background: var(--pattern-tone);
  }
  .website {
    position: absolute; left: 0; right: 0; top: 244px; text-align: center;
    font-size: 14px; font-weight: 700; color: var(--ink-dark);
  }
</style>
</head>
<body>
<div class="canvas">
  <section class="card card--front">
    <div class="wordmark">QUILLBARN</div>
    <div class="person">
      <div class="person__name">MARCUS HALE</div>
      <div class="person__title">Managing Director</div>
    </div>
    <div class="divider"></div>
    <address class="address">Addres Line Comes Here,<br>Location Pincode 45215</address>
    <ul class="contacts">
      <li>(044)123456789
        <svg viewBox="0 0 10 10"><path d="M2 0.5 L3.6 2.6 L2.8 3.6 C3.4 5 5 6.6 6.4 7.2 L7.4 6.4 L9.5 8 L8.6 9.5 C4.5 9.5 0.5 5.5 0.5 1.4 Z"/></svg>
      </li>
      <li>(044)123456780
        <svg viewBox="0 0 10 10"><path d="M2 0.5 L3.6 2.6 L2.8 3.6 C3.4 5 5 6.6 6.4 7.2 L7.4 6.4 L9.5 8 L8.6 9.5 C4.5 9.5 0.5 5.5 0.5 1.4 Z"/></svg>
      </li>
      <li>info@youremail.com
        <svg viewBox="0 0 10 10"><path d="M0.5 2 H9.5 V8.5 H0.5 Z M1 2.4 L5 5.6 L9 2.4" fill="var(--ink-soft)" stroke="var(--card-dark)" stroke-width="0.8"/></svg>
      </li>
    </ul>
  </section>

  <section class="card card--back">
    <div class="pattern-field" role="img" aria-label="Faint repeating decorative pattern covering the back of the card"></div>
    <div class="wordmark">QUILLBARN</div>
    <div class="website">www.quillbarn.com</div>
  </section>
</div>
</body>
</html>
```